Hardware Brand Packaging Design Project

We require a design for packaging for products in the retail hardware range. Initially this will be for a set of header cards for abrasive sanding discs but we plan to add other items to the range so we are looking for a range of brand elements that can be extended to other types of packaging.
The brand name is "Gleam Ridge" and we are looking for a black or dark grey background with a subtle fine pattern to break up the solid colour. This part of the design needs to be 'expandable' so that it can be used on different pack sizes as we increase the range. Two highlight or complimentary colours will add a bit of impact and become part of the brand style.
For printing purposes we have allowed for 4 colour process plus two spot colours and we have attached one of the header card dielines as a guide.
Target Market(s)
Home owners of both gender in the 25 to 55 age range
Industry/Entity Type
Printing
Requirements
Must have
- *The brand name "Gleam Ridge" should appear in the top left hand corner and we had in mind that the word would be a shiny metal / chrome appearance in could be in the shape of a shield or spear point but are open to any other suggestions.The word can be on one line or one above the other.
*Between the bottom of the hanger hole and the edge of the card is the words ABRASIVES & ACCESSORIES
*We want a performance guarantee device circle / seal or other in the bottom left quartile of the front facing panel. Circle device on attachment shows approx position.
* The right hand 25mm of the card is to be devoted to specific information about the product in the pack. This will be done by an adhered over-sticker ( see attached die-line No 2 )
* 3 line address panel or rear of card - QRT Abrasives, 47 Lane, West Auckland, New Zealand.
* Also somewhere on rear panel "Cut, Quality Checked & Packed in New Zealand from imported materials."
Nice to have
- It would be good, but not essential, to see a rough mock-up of how this design would transfer across to a box approx 80mm across the front, 100mm deep and 250mm high.

```html
<!DOCTYPE html>
<html lang="en">
<head>
<meta charset="utf-8">
<title>Gleam Ridge – Abrasives Header Card</title>
<link rel="stylesheet" href="https://fonts.googleapis.com/css2?family=Oswald:wght@700&family=Arimo:wght@400&display=swap">
<style>
  :root {
    --page-bg: #f6f6f6;
    --panel-dark-top: #1c1d20;
    --panel-dark-mid: #34373d;
    --panel-yellow-top: #c8c400;
    --panel-yellow-bottom: #f7f41c;
    --die-line: #1b2470;
    --hole-fill: #ffffff;
    --brand-text: #e4e4e4;
    --heading-text: #f2f2f2;
    --body-text: #111111;
    --seal-gold: #e3a823;
    --seal-gold-light: #f6cf5a;
  }
  html, body {
    margin: 0;
    padding: 0;
    width: 1200px;
    height: 1110px;
    overflow: hidden;
    background: var(--page-bg);
  }
  .canvas {
    display: block;
    width: 1200px;
    height: 1110px;
  }
  .brand-name {
    font-family: "Oswald", sans-serif;
    font-weight: 700;
    fill: var(--brand-text);
  }
  .range-heading {
    font-family: "Oswald", sans-serif;
    font-weight: 700;
    fill: var(--heading-text);
  }
  .origin-line {
    font-family: "Arimo", sans-serif;
    font-size: 15px;
    fill: var(--body-text);
  }
  .address-line {
    font-family: "Arimo", sans-serif;
    font-size: 9px;
    fill: var(--body-text);
  }
</style>
</head>
<body>
<svg class="canvas" viewBox="0 0 1200 1110" xmlns="http://www.w3.org/2000/svg">
  <defs>
    <linearGradient id="darkPanel" x1="0" y1="0" x2="1" y2="0.3">
      <stop offset="0" stop-color="var(--panel-dark-top)"/>
      <stop offset="0.45" stop-color="var(--panel-dark-mid)"/>
      <stop offset="1" stop-color="var(--panel-dark-top)"/>
    </linearGradient>
    <linearGradient id="yellowPanel" x1="0" y1="0" x2="0" y2="1">
      <stop offset="0" stop-color="var(--panel-yellow-top)"/>
      <stop offset="1" stop-color="var(--panel-yellow-bottom)"/>
    </linearGradient>
    <radialGradient id="sealGold" cx="0.4" cy="0.35" r="0.7">
      <stop offset="0" stop-color="var(--seal-gold-light)"/>
      <stop offset="1" stop-color="var(--seal-gold)"/>
    </radialGradient>
    <clipPath id="cardShape">
      <path d="M267,245 L368,245 A312,312 0 0 0 800,245 L898,245 A12,12 0 0 1 910,257 L910,840 A12,12 0 0 1 898,852 L800,852 A312,312 0 0 0 368,852 L267,852 A12,12 0 0 1 255,840 L255,257 A12,12 0 0 1 267,245 Z"/>
    </clipPath>
  </defs>

  <g class="header-card">
    <g clip-path="url(#cardShape)">
      <rect class="panel-dark" x="255" y="245" width="655" height="340" fill="url(#darkPanel)"/>
      <rect class="panel-yellow" x="255" y="585" width="655" height="267" fill="url(#yellowPanel)"/>
    </g>
    <path class="die-outline" d="M267,245 L368,245 A312,312 0 0 0 800,245 L898,245 A12,12 0 0 1 910,257 L910,840 A12,12 0 0 1 898,852 L800,852 A312,312 0 0 0 368,852 L267,852 A12,12 0 0 1 255,840 L255,257 A12,12 0 0 1 267,245 Z" fill="none" stroke="var(--die-line)" stroke-width="1.5"/>

    <path class="hanger-hole" d="M470,440 L645,440 A18.5,18.5 0 0 1 645,477 L603,477 A18,18 0 0 1 567,477 L553,477 A10,10 0 0 1 533,477 L515,477 A9,9 0 0 1 500,480 L452,548 L500,620 L525,620 A10,10 0 0 1 545,620 L565,620 A18,18 0 0 1 601,620 L612,620 A10,10 0 0 1 632,620 L645,620 A19,19 0 0 1 645,658 L485,658 L412,548 Z" fill="var(--hole-fill)" stroke="var(--die-line)" stroke-width="1.5"/>

    <g class="brand-lockup">
      <text class="brand-name" x="265" y="382" font-size="54" textLength="260" lengthAdjust="spacingAndGlyphs">GLEAM</text>
      <text class="brand-name" x="265" y="425" font-size="54" textLength="182" lengthAdjust="spacingAndGlyphs">RIDGE</text>
    </g>

    <text class="range-heading" x="508" y="573" font-size="40" textLength="389" lengthAdjust="spacingAndGlyphs">ABRASIVES &amp; ACCESSORIES</text>

    <text class="origin-line" x="575" y="686" text-anchor="middle">Cut, Quality Checked &amp; Packed in New Zealand from imported materials</text>

    <g class="address-panel">
      <text class="address-line" x="265" y="806">QRT Abrasives, 47 Lane,</text>
      <text class="address-line" x="265" y="817">West Auckland, New Zealand.</text>
    </g>

    <g class="guarantee-seal" role="img" aria-label="Satisfaction guarantee seal">
      <circle cx="853" cy="797" r="58" fill="url(#sealGold)"/>
      <circle cx="853" cy="797" r="44" fill="none" stroke="#ffffff" stroke-width="10" opacity="0.85"/>
    </g>
  </g>
</svg>
</body>
</html>
```